□今後強化していきたい点
・新規顧客集客
・既存顧客への情報発信
・求人

▶ターゲット
<現在>
20~30代(メイン)
40~60代まで幅広く
会社員
主婦
お子様連れ
学生
女性7:男性3

<今後>
20~30代(メイン)
会社員
主婦
学生
女性7:男性3
強化したい項目:新規顧客増、来店頻度増

-----------------------------------

<現サイトの問題点>
・更新の利便性
・情報量(専門性)
・携帯での導線

<最大の要望は?>
①デザイン性の向上
②操作性の向上
③店舗の強みの打ち出し

<ホームページに期待する効果>
・求職者向け
・既存顧客むけ
・求職者向け

◆サイトマップ
1.TOP
∟2.サロンコンセプト★
∟3.1店舗目情報ページ
∟4.2店舗目情報ページ
∟5.スタッフ一覧★
∟6.スタッフ詳細
∟7.スタイルギャラリー一覧★
∟8.スタイルギャラリー詳細
∟9.メニュー一覧
∟10.プロダクト一覧
∟11.求人情報①店舗について、先輩スタッフインタビューなど★
∟12.求人情報②募集要項★
∟13.ニュース一覧★
∟14.ニュース詳細
∟15.ブログ一覧★
∟16.ブログ詳細
∟17.トリートメント、ヘアケアについて★

※★がついている項目についてはTOPページへ入り口を配置頂きたい項目になります。
(よりよい構成がございましたら、どうぞご自由にご提案ください。)

【参考サイト】
https://kiro-lashworks.com/

http://dunmoth.com/
→デザインをされる際に、こちらのサイトのように
スタッフ紹介部分を写真の切り抜きで構成をお願い致します。

https://roi-te.com/

■デザインのテイスト
カジュアル、ナチュラル、モダン
シンプルでわかりやすさは残しつつ、
ワンポイントでイラストや画像の切り抜き、飾り枠などを使用するなど、
センスよく少しにぎやかな雰囲気にしたいと考えております。

■補足説明
【ダミーテキストについて】
・極力サイト内の文章を配置下さい。
ブログ・ニュースのタイトル部分などは
「タイトルが入ります。」で大丈夫です。
「ここに文章が入ります。ここに文章が入ります。」などの
同じ文章を繰り返したダミー文章は極力使用しないようお願いいたします。
また、フォントに関しては読み込み速度等の観点から、
ウェブフォントの使用は避けて頂けますと幸いです。

※業務への支障がでる可能性がございますので、
電話でのご連絡はご遠慮頂いております。
http://mil-e-vo.tokyo/salon
茶系、緑系、ベースカラーは白、 差し色はブラウン系かグリーン系の色 グレーの使用はご遠慮頂けますと幸いです。
◆素材について
①素材として必要なものがある場合には、ミラフォトバンク画像をご使用ください。
その際、定期契約でダウンロード出来る画像のみを使用してください。
ミラフォトバンク以外の素材を使用する際には、
必ず無料で提供いただける物のみご使用ください。
ミラフォトバンク: https://pics.mirafoto.com/jp/

【院内写真、ロゴについて】
院内写真などの素材については下記URLよりダウンロードをお願い致します。
https://58.sendcrate.nu/4417-f0a9d2e61b7c34a8e5d90b2c1f6a7e4d5
https://58.sendcrate.nu/4417-d83e0c5a92f14b6e7a1c08d5e3b9f2c71
https://58.sendcrate.nu/4417-k2a9e5c710b6d4f38c1e9a07d6b4e5f93
更に多くのデザインを見たいと考えておりますので、
募集期間を延長させて頂きます。

どうぞ自由な発想でのご提案をお待ちしております。

以上、何卒宜しくお願い致します。
更に多くのデザインを見たいと考えておりますので、
募集期間を延長させて頂きます。

どうぞ自由な発想でのご提案をお待ちしております。

以上、何卒宜しくお願い致します。

サロンの雰囲気と合致していたため

この度はご提案を頂きありがとうございました。

```html
<!DOCTYPE html>
<html lang="ja">
<head>
<meta charset="utf-8">
<title>mil e vo Beauty salon</title>
<link rel="stylesheet" href="https://fonts.googleapis.com/css2?family=Josefin+Sans:wght@300;400;600&family=Noto+Sans+JP:wght@300;400;500&display=swap">
<style>
:root{
  --base:#f5f7ef;
  --band:#dde8cc;
  --tile:#dfe9cf;
  --green:#6c9f3c;
  --green-dark:#4e7d27;
  --brown:#4a3a2f;
  --text:#3d342d;
  --line:#b9b0a6;
  --white:#ffffff;
}
*{margin:0;padding:0;box-sizing:border-box}
html,body{width:1200px;height:4236px;overflow:hidden}
body{background:var(--base);color:var(--text);font-family:"Noto Sans JP",sans-serif;position:relative;font-size:14px}
.abs{position:absolute}
.ph{position:absolute}
.en{font-family:"Josefin Sans",sans-serif}
.sec-title{position:absolute;font-family:"Josefin Sans",sans-serif;font-weight:400;font-size:34px;letter-spacing:3px;color:var(--brown)}
.body-text{position:absolute;font-size:13px;line-height:2;color:var(--text)}
.more-bracket{position:absolute;width:150px;height:56px;border-left:1px solid var(--brown);border-right:1px solid var(--brown);font-family:"Josefin Sans",sans-serif;font-size:12px;letter-spacing:2px;display:flex;align-items:center;justify-content:center;color:var(--brown)}
.more-line{position:absolute;font-family:"Josefin Sans",sans-serif;font-size:12px;letter-spacing:2px;color:var(--brown);border-bottom:1px solid var(--brown);padding:0 0 6px 60px}

/* hero */
.hero-photo{left:420px;top:0;width:780px;height:560px;background:linear-gradient(100deg,#f5f7ef 0%,#ece6df 30%,#d9c7b8 60%,#c9b2a0 100%)}
.brand{left:190px;top:140px;font-family:"Josefin Sans",sans-serif;font-weight:300;font-size:64px;letter-spacing:8px;color:#8a7d72}
.brand-sub{left:250px;top:236px;font-family:"Josefin Sans",sans-serif;font-size:30px;color:var(--green);letter-spacing:1px}
.leaf-art{left:120px;top:185px;width:150px;height:130px;background:radial-gradient(ellipse at center,#9cc36e 0%,#bcd89a 55%,rgba(188,216,154,0) 75%)}
.tagline{left:170px;top:298px;font-family:"Josefin Sans",sans-serif;font-size:34px;line-height:1.25;color:var(--brown)}
.tagline::before{content:"";display:inline-block;width:40px;height:1px;background:var(--brown);vertical-align:middle;margin-right:14px}
.contact-tab{left:1152px;top:140px;width:48px;height:190px;background:var(--green);color:#fff;font-family:"Josefin Sans",sans-serif;font-size:14px;letter-spacing:2px;writing-mode:vertical-rl;display:flex;align-items:center;justify-content:center}
.menu-btn{left:1152px;top:20px;width:40px;height:40px}

/* news */
.news-label{left:185px;top:566px;font-family:"Josefin Sans",sans-serif;font-weight:600;font-size:22px;color:var(--green);letter-spacing:2px}
.news-list{left:290px;top:530px;width:720px;list-style:none}
.news-list li{height:46px;border-bottom:1px solid var(--line);display:flex;align-items:center;justify-content:space-between;font-size:12.5px}
.news-list .date{margin-right:16px}
.news-more{left:930px;top:606px}

/* concept */
.concept-band{left:0;top:780px;width:1200px;height:360px;background:var(--band)}
.concept-photo{left:170px;top:750px;width:260px;height:370px;background:linear-gradient(160deg,#f4e6cf,#e2b98a 55%,#b9895d)}
.concept-title{left:470px;top:790px}
.concept-text{left:470px;top:850px;width:560px}
.btn-dark{position:absolute;left:660px;top:1068px;width:120px;height:34px;background:var(--brown);color:#fff;font-family:"Josefin Sans",sans-serif;font-size:12px;letter-spacing:2px;display:flex;align-items:center;justify-content:center}

/* topics */
.topics-title{left:165px;top:1290px}
.topics-text{left:165px;top:1350px;width:580px}
.topics-more{left:270px;top:1500px}
.topics-photo{left:780px;top:1290px;width:260px;height:270px;background:linear-gradient(170deg,#e8e0da,#8b6a52 60%,#4e3a2c)}

/* gallery */
.gallery-title{left:165px;top:1680px}
.gallery-nav{left:930px;top:1690px;width:110px;height:20px}
.gallery-item{position:absolute;top:1740px;width:200px}
.gallery-item .img{height:220px}
.gallery-item p{font-size:11px;margin-top:10px;color:var(--text)}

/* salon */
.salon-title{left:165px;top:2165px}
.salon-photo{left:165px;top:2225px;width:370px;height:180px;background:linear-gradient(180deg,#dcd6cc,#f0ece4 50%,#9e8f7c)}
.salon-info{left:615px;top:2225px;font-size:12.5px;line-height:1.9}
.salon-info .name{font-family:"Josefin Sans",sans-serif;font-size:18px;margin-bottom:6px}
.salon-more{left:715px;top:2430px}

/* staff */
.staff-title{left:165px;top:2575px}
.staff-card{position:absolute;width:235px;height:210px;background:var(--tile)}
.staff-cut{position:absolute;left:-10px;top:-30px;width:110px;height:250px;background:linear-gradient(180deg,#c9a98a,#8a6a52 50%,#3f352f);border-radius:50px 50px 8px 8px}
.staff-name{position:absolute;right:18px;bottom:30px;text-align:right;font-size:15px;letter-spacing:2px}
.staff-name small{display:block;font-family:"Josefin Sans",sans-serif;font-size:12px;letter-spacing:1px;margin-top:4px}

/* recruit */
.recruit-band{left:0;top:3290px;width:1200px;height:190px;background:var(--white)}
.recruit-label{left:175px;top:3320px;font-family:"Josefin Sans",sans-serif;font-weight:600;font-size:22px;color:var(--green);letter-spacing:1px}
.recruit-text{left:310px;top:3315px;width:690px}
.recruit-more{left:540px;top:3425px;font-family:"Josefin Sans",sans-serif;font-size:13px;color:var(--brown);letter-spacing:2px}

/* blog */
.blog-title{left:165px;top:3630px}
.blog-card{position:absolute;top:3695px;width:250px}
.blog-card .img{height:190px;background:var(--white);display:flex;flex-direction:column;align-items:center;justify-content:center}
.blog-card .img .mark{font-family:"Josefin Sans",sans-serif;font-size:26px;color:var(--brown)}
.blog-card .img .note{font-size:13px;color:#b3462e;margin-top:6px}
.blog-card .date{font-size:12px;margin-top:14px}
.blog-card h3{font-size:15px;font-weight:500;margin-top:4px}
.blog-card p{font-size:11.5px;line-height:1.8;margin-top:8px}
.blog-card .bmore{display:block;margin-top:34px;text-align:right;font-family:"Josefin Sans",sans-serif;font-size:11px;letter-spacing:2px;border-bottom:1px solid var(--brown);padding-bottom:6px}

.footer{left:0;top:4200px;width:1200px;height:36px;background:var(--brown);color:#e9e2d8;font-family:"Josefin Sans",sans-serif;font-size:11px;display:flex;align-items:center;justify-content:center;letter-spacing:1px}
</style>
</head>
<body>

<header>
  <div class="ph hero-photo" role="img" aria-label="Portrait photograph of a salon model with soft brown hair"></div>
  <div class="ph leaf-art" role="img" aria-label="Green leaf vine illustration"></div>
  <div class="abs brand">MIL E VO</div>
  <div class="abs brand-sub">Beauty salon</div>
  <div class="abs tagline">Every Day is An<br>&nbsp;&nbsp;&nbsp;&nbsp;&nbsp;&nbsp;&nbsp;&nbsp;&nbsp;&nbsp;&nbsp;&nbsp;&nbsp;Anniversary</div>
  <svg class="abs menu-btn" viewBox="0 0 40 40"><g stroke="#4a3a2f" stroke-width="2"><line x1="8" y1="12" x2="32" y2="12"/><line x1="8" y1="20" x2="32" y2="20"/><line x1="8" y1="28" x2="32" y2="28"/></g></svg>
  <div class="abs contact-tab">Contact Us</div>
</header>

<section class="news">
  <div class="abs news-label">NEWS</div>
  <ul class="abs news-list">
    <li><span><span class="date">2020.5.8</span>緊急事態宣言の延長を受けミルエヴォは営業時間を19時までに短縮営業致します</span><span>›</span></li>
    <li><span><span class="date">2020.5.8</span>緊急事態宣言の延長を受けミルエヴォは営業時間を19時までに短縮営業致します</span><span>›</span></li>
  </ul>
  <div class="more-line news-more">MORE</div>
</section>

<section class="concept">
  <div class="abs concept-band"></div>
  <div class="ph concept-photo" role="img" aria-label="Salon interior with orange chairs and mirrors"></div>
  <div class="sec-title concept-title">CONCEPT</div>
  <p class="body-text concept-text">店名は「毎日が記念日」をコンセプトにお客様の人生を彩る空間です。<br>「mil e vo」とはフランス語で「一歩一歩」のように歩むという意味です。一日一日を大切に<br>したがら一歩一歩着実に前に進む、そんなサロンを目指しています。この名前があらわすように、<br>楽しい記念日をいつでもお過ごしいただけます。ぜひ気軽に遊びに来てください。</p>
  <div class="btn-dark">MORE</div>
</section>

<section class="topics">
  <div class="sec-title topics-title">TOPICS</div>
  <p class="body-text topics-text">お客様の髪の毛を大事に考えたダメージレス薬剤選びをしています。<br>カラー剤もこだわり、オーガニック成分配合の優しい仕上がりを実現。<br>季節ごとの髪の悩みに寄り添い、自宅でのケア方法もお伝えします。<br>ヘアケアアイテムも豊富に揃えてお待ちしております。</p>
  <div class="more-bracket topics-more">MORE</div>
  <div class="ph topics-photo" role="img" aria-label="Close-up of long straight brown hair"></div>
</section>

<section class="gallery">
  <div class="sec-title gallery-title">GALLERY</div>
  <svg class="abs gallery-nav" viewBox="0 0 110 20"><g stroke="#4a3a2f" stroke-width="1.5" fill="none"><line x1="0" y1="10" x2="40" y2="10"/><polyline points="8,4 0,10 8,16"/><line x1="70" y1="10" x2="110" y2="10"/><polyline points="102,4 110,10 102,16"/></g></svg>
  <div class="gallery-item" style="left:165px"><div class="img" style="background:linear-gradient(180deg,#e6e1da,#7d5f47 60%,#3c3028)" role="img" aria-label="Short hairstyle sample"></div><p>mil e vo ショートスタイル</p></div>
  <div class="gallery-item" style="left:390px"><div class="img" style="background:linear-gradient(180deg,#e9e4dc,#b08a68 60%,#6b5241)" role="img" aria-label="Medium hairstyle sample"></div><p>mil e vo ミディアムスタイル</p></div>
  <div class="gallery-item" style="left:615px"><div class="img" style="background:linear-gradient(180deg,#ebe6dd,#9b7a5e 60%,#4d3b2e)" role="img" aria-label="Arranged updo hairstyle sample"></div><p>mil e vo アレンジスタイル</p></div>
  <div class="gallery-item" style="left:840px"><div class="img" style="background:linear-gradient(180deg,#e4dcd2,#6e4e3a 60%,#2f241d)" role="img" aria-label="Long hairstyle sample"></div><p>mil e vo ロングスタイル</p></div>
</section>

<section class="salon">
  <div class="sec-title salon-title">SALON</div>
  <div class="ph salon-photo" role="img" aria-label="Salon storefront with large windows"></div>
  <div class="abs salon-info">
    <div class="name">mil e vo</div>
    〒182-0000<br>
    東京都みどり市若葉町3-8 ソラビル1F<br>
    OPEN　10:00〜21:00（最終受付20:00）<br>
    CLOSE　毎週火曜日<br>
    TEL　042-000-0148
  </div>
  <div class="more-bracket salon-more">MORE</div>
</section>

<section class="staff">
  <div class="sec-title staff-title">STAFF</div>
  <div class="staff-card" style="left:165px;top:2645px"><div class="staff-cut" role="img" aria-label="Cutout photo of staff member"></div><div class="staff-name">ハヤマ ケイタ<small>Shop manager</small></div></div>
  <div class="staff-card" style="left:462px;top:2645px"><div class="staff-cut" role="img" aria-label="Cutout photo of staff member"></div><div class="staff-name">ミナセ ヒロキ<small>Chief</small></div></div>
  <div class="staff-card" style="left:760px;top:2645px"><div class="staff-cut" role="img" aria-label="Cutout photo of staff member"></div><div class="staff-name">タカノ ソウタ<small>Stylist</small></div></div>
  <div class="staff-card" style="left:165px;top:2955px"><div class="staff-cut" role="img" aria-label="Cutout photo of staff member"></div><div class="staff-name">オオノ アヤメ<small>Stylist</small></div></div>
  <div class="staff-card" style="left:462px;top:2955px"><div class="staff-cut" role="img" aria-label="Cutout photo of staff member"></div><div class="staff-name">ミズキ サヤカ<small>Assistant</small></div></div>
  <div class="staff-card" style="left:760px;top:2955px"><div class="staff-cut" role="img" aria-label="Cutout photo of staff member"></div><div class="staff-name">クボ ユカ<small>Assistant</small></div></div>
</section>

<section class="recruit">
  <div class="abs recruit-band"></div>
  <div class="abs recruit-label">Recruit</div>
  <p class="body-text recruit-text">「mil e vo」とはフランス語で一歩一歩という意味です。一日一日を大切にしながら一歩一歩着実に<br>進んで行くというコンセプトのとおり、スタッフの成長を一歩一歩大切にし、スキルアップを応援して<br>います。美容師の経験がある方もない方も「mil e vo」で働きませんか？皆さまのご応募をお待ちし<br>ております。</p>
  <div class="abs recruit-more">more　→</div>
</section>

<section class="blog">
  <div class="sec-title blog-title">BLOG</div>
  <article class="blog-card" style="left:165px"><div class="img"><span class="mark">mil e vo</span><span class="note">営業時間短縮のおしらせ</span></div><div class="date">2020.5.8</div><h3>営業時間短縮のおしらせ</h3><p>緊急事態宣言の延長を受けミルエヴォは営業時間を19時までに短縮営業いたします。ご理解のほどよろしくお願いいたします。</p><span class="bmore">MORE</span></article>
  <article class="blog-card" style="left:475px"><div class="img"><span class="mark">mil e vo</span><span class="note">営業時間短縮のおしらせ</span></div><div class="date">2020.5.8</div><h3>営業時間短縮のおしらせ</h3><p>緊急事態宣言の延長を受けミルエヴォは営業時間を19時までに短縮営業いたします。ご理解のほどよろしくお願いいたします。</p><span class="bmore">MORE</span></article>
  <article class="blog-card" style="left:785px"><div class="img"><span class="mark">mil e vo</span><span class="note">営業時間短縮のおしらせ</span></div><div class="date">2020.5.8</div><h3>営業時間短縮のおしらせ</h3><p>緊急事態宣言の延長を受けミルエヴォは営業時間を19時までに短縮営業いたします。ご理解のほどよろしくお願いいたします。</p><span class="bmore">MORE</span></article>
</section>

<footer class="abs footer">Copyright © 2020 mil e vo All Rights Reserved.</footer>

</body>
</html>
```